Trade show Banner to be displayed on vertical stand

We are an IT company that specializes in working with Manufacturing companies and manufacturing plants. We need two banners designed for a manufacturing trade show. The design needs to be designed using the supplied template file. Also the design needs to communicate graphically that we specialize in working with manufacturing plants. Also they should communicate that out services include: IT Services, Network, Voice, Data

Target Market(s)

Manufacturing companies

Industry/Entity Type

Manufacturing

Requirements
Must have
• Clear message, clear graphic message. Must be designed with included templates
Nice to have
• Company colors need to be used, but additional colors can be used

```html
<!DOCTYPE html>
<html lang="en">
<head>
<meta charset="UTF-8">
<title>gridline works – Trade Show Banners</title>
<link rel="stylesheet" href="https://fonts.googleapis.com/css2?family=Bebas+Neue&family=Open+Sans:wght@400;600;700&display=swap">
<style>
  :root {
    --brand-blue: #1b74c0;
    --deep-blue: #1565ad;
    --light-blue: #8ec3ea;
    --brand-orange: #f07f22;
    --ink: #1d1d1f;
    --body-ink: #333;
    --paper: #ffffff;
    --backdrop: #e4e4e4;
  }
  * { box-sizing: border-box; margin: 0; padding: 0; }
  html, body { width: 1112px; height: 1200px; overflow: hidden; }
  body { background: var(--backdrop); font-family: "Open Sans", Arial, sans-serif; position: relative; }

  .banner {
    position: absolute; width: 290px; height: 900px;
    background: var(--paper); overflow: hidden;
    box-shadow: 0 8px 24px rgba(0,0,0,.12);
  }
  .banner--intro { left: 205px; top: 150px; }
  .banner--services { left: 620px; top: 130px; }
  .banner__shapes { position: absolute; inset: 0; }

  .brand { position: absolute; display: flex; align-items: center; gap: 10px; }
  .brand__dot { width: 40px; height: 40px; border-radius: 50%; background: var(--brand-blue); flex: none; }
  .brand__name { font-family: "Open Sans", Arial, sans-serif; font-weight: 700; font-size: 27px; color: var(--brand-blue); letter-spacing: .5px; line-height: 1; white-space: nowrap; }
  .brand--top { left: 24px; top: 52px; }
  .brand--bottom { left: 52px; top: 728px; }
  .brand--bottom .brand__dot { background: var(--paper); width: 34px; height: 34px; }
  .brand--bottom .brand__name { color: var(--paper); font-size: 24px; }

  .badge {
    position: absolute; color: var(--paper); font-weight: 600; text-align: center;
    font-size: 22px; line-height: 1.45;
  }
  .badge--left { left: 0; top: 470px; width: 110px; }
  .badge--right { left: 172px; top: 222px; width: 118px; font-size: 21px; }

  .pitch { position: absolute; left: 18px; top: 636px; width: 262px; }
  .pitch__headline {
    font-family: "Bebas Neue", Impact, sans-serif; font-weight: 400; color: var(--paper);
    font-size: 35px; line-height: 1.08; letter-spacing: 1px;
  }
  .pitch__headline em { font-style: normal; color: var(--brand-orange); }
  .pitch__note { margin-top: 6px; color: var(--paper); font-size: 11.5px; letter-spacing: .2px; white-space: nowrap; }
  .pitch__note em { font-style: normal; color: var(--brand-orange); }

  .url-pill {
    position: absolute; height: 28px; border-radius: 8px; background: var(--brand-orange);
    color: var(--paper); font-weight: 700; font-size: 13px; letter-spacing: 1.5px;
    display: flex; align-items: center; justify-content: center; white-space: nowrap;
  }
  .url-pill--intro { left: 58px; top: 812px; width: 156px; }
  .url-pill--services { left: 62px; top: 770px; width: 152px; }

  .services__title {
    position: absolute; left: 0; top: 335px; width: 290px; text-align: center;
    font-family: "Bebas Neue", Impact, sans-serif; font-weight: 400; font-size: 34px; letter-spacing: 1px; color: var(--ink);
  }
  .services__title span { color: var(--brand-blue); }
  .services__rule { position: absolute; left: 72px; top: 378px; width: 146px; height: 1px; background: var(--brand-orange); }

  .service { position: absolute; width: 140px; text-align: center; }
  .service__icon {
    width: 48px; height: 48px; margin: 0 auto; border: 2px solid var(--brand-orange);
    border-radius: 50%; display: flex; align-items: center; justify-content: center;
  }
  .service__icon svg { width: 24px; height: 24px; }
  .service__name {
    font-family: "Bebas Neue", Impact, sans-serif; font-weight: 400; color: var(--brand-blue);
    font-size: 16px; letter-spacing: .5px; margin-top: 12px; line-height: 1;
  }
  .service__text { font-size: 8.5px; line-height: 1.3; color: var(--body-ink); margin-top: 3px; }
  .service--it { left: 2px; top: 396px; }
  .service--security { left: 136px; top: 400px; width: 150px; }
  .service--cloud { left: 2px; top: 536px; }
  .service--voice { left: 136px; top: 550px; width: 150px; }
</style>
</head>
<body>

<section class="banner banner--intro" aria-label="Banner one: support pitch">
  <svg class="banner__shapes" viewBox="0 0 290 900" width="290" height="900">
    <defs>
      <linearGradient id="workerTones" x1="0" y1="0" x2="1" y2="1">
        <stop offset="0" stop-color="#6b6f73"/>
        <stop offset=".45" stop-color="#c98a3a"/>
        <stop offset=".75" stop-color="#8aa24a"/>
        <stop offset="1" stop-color="#3a3d40"/>
      </linearGradient>
    </defs>
    <path d="M0 142 Q145 118 290 162" fill="none" stroke="var(--light-blue)" stroke-width="6"/>
    <path d="M0 146 Q145 122 290 166 L290 560 Q150 565 0 590 Z" fill="url(#workerTones)" role="img" aria-label="Photo: factory technician in hard hat and safety vest checking a tablet on the plant floor"/>
    <path d="M0 582 Q150 555 290 552 L290 900 L0 900 Z" fill="var(--light-blue)"/>
    <path d="M0 592 Q150 566 290 566 L290 900 L0 900 Z" fill="var(--brand-blue)"/>
    <rect x="30" y="700" width="170" height="150" rx="28" fill="var(--deep-blue)" opacity=".45"/>
    <circle cx="52" cy="510" r="62" fill="var(--brand-orange)" opacity=".95"/>
    <circle cx="82" cy="568" r="22" fill="var(--brand-orange)" opacity=".9"/>
  </svg>

  <div class="brand brand--top"><span class="brand__dot"></span><span class="brand__name">gridline works</span></div>

  <div class="badge badge--left">24x7<br>SUPPORT</div>

  <div class="pitch">
    <h1 class="pitch__headline">Looking <em>for</em> better,<br>computer &amp; network<br>support?</h1>
    <p class="pitch__note">DON'T WAIT. WE CAN HELP YOU <em>RIGHT NOW!</em></p>
  </div>
  <div class="url-pill url-pill--intro">WWW.GLWX.COM</div>
</section>

<section class="banner banner--services" aria-label="Banner two: services overview">
  <svg class="banner__shapes" viewBox="0 0 290 900" width="290" height="900">
    <defs>
      <linearGradient id="serverTones" x1="0" y1="0" x2="1" y2="0">
        <stop offset="0" stop-color="#1f2a33"/>
        <stop offset=".4" stop-color="#2f6f8a"/>
        <stop offset=".7" stop-color="#c9ccd0"/>
        <stop offset="1" stop-color="#e6e6e6"/>
      </linearGradient>
    </defs>
    <path d="M0 0 H290 V262 Q150 296 0 282 Z" fill="url(#serverTones)" role="img" aria-label="Photo: IT engineer with a tablet beside a server rack full of network cabling"/>
    <path d="M0 284 Q150 298 290 264" fill="none" stroke="var(--light-blue)" stroke-width="5"/>
    <circle cx="236" cy="262" r="68" fill="var(--brand-orange)" opacity=".95"/>
    <path d="M0 712 Q140 660 290 672 L290 900 L0 900 Z" fill="var(--light-blue)"/>
    <path d="M0 724 Q140 676 290 686 L290 900 L0 900 Z" fill="var(--brand-blue)"/>
    <rect x="40" y="720" width="90" height="100" rx="22" fill="var(--deep-blue)" opacity=".5"/>
    <rect x="150" y="770" width="90" height="110" rx="22" fill="var(--deep-blue)" opacity=".5"/>
  </svg>

  <div class="badge badge--right">24x7<br>SUPPORT</div>

  <h2 class="services__title">What we <span>do</span></h2>
  <div class="services__rule"></div>

  <div class="service service--it">
    <div class="service__icon">
      <svg viewBox="0 0 24 24" fill="none" stroke="var(--brand-orange)" stroke-width="2"><circle cx="9" cy="14" r="4"/><path d="M9 7v2M9 19v2M2 14h2M14 14h2M4 9l1.5 1.5M12.5 17.5L14 19M4 19l1.5-1.5M12.5 10.5L14 9"/><circle cx="18" cy="6" r="2.5"/></svg>
    </div>
    <div class="service__name">Managed IT Service</div>
    <p class="service__text">24/7 Proactive IT Support from<br>a friendly knowledgeable<br>team of experts.</p>
  </div>

  <div class="service service--security">
    <div class="service__icon">
      <svg viewBox="0 0 24 24" fill="none" stroke="var(--brand-orange)" stroke-width="2"><ellipse cx="12" cy="5" rx="7" ry="2.5"/><path d="M5 5v14c0 1.4 3.1 2.5 7 2.5s7-1.1 7-2.5V5M5 10c0 1.4 3.1 2.5 7 2.5s7-1.1 7-2.5M5 14.5c0 1.4 3.1 2.5 7 2.5s7-1.1 7-2.5"/></svg>
    </div>
    <div class="service__name">Data Security</div>
    <p class="service__text">Ransomware and Human Error<br>threaten your data every day.<br>Make sure your business is protected.</p>
  </div>

  <div class="service service--cloud">
    <div class="service__icon">
      <svg viewBox="0 0 24 24" fill="var(--brand-orange)"><path d="M7 18a4 4 0 0 1-.6-7.96A5.5 5.5 0 0 1 17 9a4.5 4.5 0 0 1 .5 9z"/></svg>
    </div>
    <div class="service__name">Cloud</div>
    <p class="service__text">From Suite 365<br>to SkyStack increase reliability<br>while reducing your IT budget.</p>
  </div>

  <div class="service service--voice">
    <div class="service__icon">
      <svg viewBox="0 0 24 24" fill="none" stroke="var(--brand-orange)" stroke-width="2"><rect x="9" y="3" width="6" height="11" rx="3" fill="var(--brand-orange)"/><path d="M5.5 11a6.5 6.5 0 0 0 13 0M12 17.5V21M9 21h6"/></svg>
    </div>
    <div class="service__name">Voice</div>
    <p class="service__text">VOIP hosted services bring<br>features and flexibility while<br>saving your business money.</p>
  </div>

  <div class="brand brand--bottom"><span class="brand__dot"></span><span class="brand__name">gridline works</span></div>
  <div class="url-pill url-pill--services">WWW.GLWX.COM</div>
</section>

</body>
</html>
```